International wholesale business needs a business card

We need a business card.

Company Details:
Company Name and logo
Address, Phone number, Website
Employee Details:
Name, Designation, Mobile Number & Email address

Logo file is attached.

```html
<!DOCTYPE html>
<html lang="en">
<head>
<meta charset="utf-8">
<title>Corvane Trading – Business Card</title>
<link href="https://fonts.googleapis.com/css2?family=Montserrat:wght@300;400;600;700&display=swap" rel="stylesheet">
<style>
  :root{
    --brand-red:#c4262e;
    --ink-gray:#8a8d91;
    --paper:#ffffff;
    --stage:#2b2b2d;
  }
  *{box-sizing:border-box;margin:0;padding:0}
  html,body{width:1200px;height:1024px;overflow:hidden}
  body{
    background:var(--stage);
    font-family:'Montserrat',sans-serif;
    display:flex;flex-direction:column;align-items:center;justify-content:center;gap:56px;
  }
  .card{width:630px;height:360px;position:relative;overflow:hidden;box-shadow:0 10px 28px rgba(0,0,0,.45)}

  /* Front */
  .card--front{background:var(--paper)}
  .front__wordmark{position:absolute;left:40px;top:72px;width:200px;text-align:center;
    color:var(--brand-red);font-weight:700;font-size:26px;line-height:1.2;letter-spacing:1px}
  .company{position:absolute;left:268px;top:42px}
  .company__name{color:var(--brand-red);font-weight:700;font-size:25px;letter-spacing:.5px;line-height:1}
  .company__address{color:var(--ink-gray);font-weight:300;font-size:15px;line-height:1.45;margin-top:12px}
  .contact-list{list-style:none;margin-top:10px}
  .contact-list li{display:flex;align-items:center;gap:8px;font-size:15px;font-weight:300;line-height:1.6;white-space:nowrap}
  .company .contact-list li{color:var(--ink-gray)}
  .company .contact-list svg{fill:var(--brand-red)}
  .front__band{position:absolute;left:0;right:0;bottom:0;height:128px;background:var(--brand-red);
    display:flex;align-items:center;padding:0 34px 0 40px;color:var(--paper)}
  .employee{padding-right:22px;border-right:1px solid rgba(255,255,255,.8)}
  .employee__name{font-weight:700;font-size:24px;letter-spacing:.5px;white-space:nowrap}
  .employee__role{font-weight:300;font-size:17px;margin-top:2px;padding-left:56px;white-space:nowrap}
  .front__band .contact-list{margin:0 0 0 22px}
  .front__band .contact-list li{color:var(--paper);font-size:16px}
  .front__band .contact-list svg{fill:var(--paper)}

  /* Back */
  .card--back{background:var(--brand-red);display:flex;align-items:center;justify-content:center;color:var(--paper)}
  .back__name{font-weight:600;font-size:42px;letter-spacing:2px;white-space:nowrap}
</style>
</head>
<body>
  <section class="card card--front">
    <p class="front__wordmark">CORVANE<br>TRADING</p>
    <div class="company">
      <h1 class="company__name">CORVANE TRADING</h1>
      <p class="company__address">4820 Harbor Point Dr. Suite 210<br>Austin, TX 78701</p>
      <ul class="contact-list">
        <li><svg width="13" height="13" viewBox="0 0 24 24"><path d="M6.6 10.8a15 15 0 0 0 6.6 6.6l2.2-2.2c.3-.3.7-.4 1-.2 1.1.4 2.3.6 3.6.6.6 0 1 .4 1 1V20c0 .6-.4 1-1 1A17 17 0 0 1 3 4c0-.6.4-1 1-1h3.5c.6 0 1 .4 1 1 0 1.3.2 2.5.6 3.6.1.3 0 .7-.2 1z"/></svg>555-014-2290</li>
        <li><svg width="13" height="13" viewBox="0 0 24 24"><path d="M12 2a10 10 0 1 0 0 20 10 10 0 0 0 0-20zm6.9 6h-3a15 15 0 0 0-1.4-3.9A8 8 0 0 1 18.9 8zM12 4c.8 1.2 1.5 2.5 1.9 4h-3.8c.4-1.5 1.1-2.8 1.9-4zM4.3 14a8 8 0 0 1 0-4h3.4a16 16 0 0 0 0 4zm.8 2h3a15 15 0 0 0 1.4 3.9A8 8 0 0 1 5.1 16zm3-8h-3a8 8 0 0 1 4.4-3.9C8.9 5.3 8.4 6.6 8.1 8zM12 20c-.8-1.2-1.5-2.5-1.9-4h3.8c-.4 1.5-1.1 2.8-1.9 4zm2.3-6H9.7a14 14 0 0 1 0-4h4.6a14 14 0 0 1 0 4zm.2 5.9c.6-1.2 1.1-2.5 1.4-3.9h3a8 8 0 0 1-4.4 3.9zm1.8-5.9a16 16 0 0 0 0-4h3.4a8 8 0 0 1 0 4z"/></svg>www.corvanetrading.com</li>
      </ul>
    </div>
    <div class="front__band">
      <div class="employee">
        <h2 class="employee__name">EMPLOYEE NAME</h2>
        <p class="employee__role">Managing Member</p>
      </div>
      <ul class="contact-list">
        <li><svg width="13" height="13" viewBox="0 0 24 24"><path d="M6.6 10.8a15 15 0 0 0 6.6 6.6l2.2-2.2c.3-.3.7-.4 1-.2 1.1.4 2.3.6 3.6.6.6 0 1 .4 1 1V20c0 .6-.4 1-1 1A17 17 0 0 1 3 4c0-.6.4-1 1-1h3.5c.6 0 1 .4 1 1 0 1.3.2 2.5.6 3.6.1.3 0 .7-.2 1z"/></svg>555-014-2290</li>
        <li><svg width="13" height="13" viewBox="0 0 24 24"><path d="M2 5h20v14H2zm2 2v.5l8 5 8-5V7zm0 2.8V17h16V9.8l-8 5z"/></svg>info@corvanetrading.com</li>
      </ul>
    </div>
  </section>

  <section class="card card--back">
    <p class="back__name">CORVANE TRADING</p>
  </section>
</body>
</html>
```